TAVRO Kiosk Webpage Design

Just need a simple, single page web design. I have a preliminary idea of what I need, just want to add a professional touch to it. We already have the google map locator plug-in. Generic website is already up and I can send the locator plugin when project is complete for final HTML/CSS Coding. Needs to be coded as a responsive design on a flexible grid (i.e. will auto adjust screen for desktop/tablet/mobile devices)
Target Market(s)
Business/Student/General Public, Mobile Office Kiosk Rental Station (Technology-Printing-Scanning-Faxing, etc...)
Industry/Entity Type
It Professional
Coding
Coded - Design and coding required
Number of Pages Required
1 page
Look and feel
Each slider illustrates characteristics of the customer's brand and the style your logo design should communicate.

```html
<!DOCTYPE html>
<html lang="en">
<head>
<meta charset="utf-8">
<title>TAVRO Kiosk</title>
<link href="https://fonts.googleapis.com/css2?family=Arimo:wght@400;700&display=swap" rel="stylesheet">
<style>
:root{
  --brand:#0b5e9c;
  --brand-dark:#084b7e;
  --ink:#222;
  --muted:#555;
  --soft:#e8ecef;
  --tab:#d9dde1;
  --white:#fff;
  --footer-dark:#1e1e1e;
  --social:#6f7a85;
}
*{box-sizing:border-box;margin:0;padding:0}
html,body{width:1200px;height:2542px;overflow:hidden}
body{font-family:"Arimo",Arial,sans-serif;color:var(--ink);background:var(--white);position:relative}

/* header */
.site-header{position:absolute;left:0;top:0;width:1200px;height:136px;background:var(--white)}
.brand{position:absolute;left:110px;top:40px;display:flex;align-items:center;gap:12px;font-size:34px;font-weight:700;color:var(--brand);letter-spacing:1px}
.brand-mark{width:26px;height:26px;background:var(--brand)}
.header-phone{position:absolute;left:774px;top:30px;display:flex;align-items:center;gap:10px;font-size:20px;color:var(--ink)}
.social{position:absolute;left:950px;top:29px;display:flex;gap:6px}
.social span{width:30px;height:30px;background:var(--social);display:block}
.main-nav{position:absolute;left:459px;top:81px;display:flex;font-size:15px}
.main-nav a{display:block;height:34px;line-height:34px;color:var(--ink);text-decoration:none;padding:0 14px;margin-right:36px}
.main-nav a.active{background:var(--brand);color:var(--white);margin-right:34px}

/* hero */
.hero{position:absolute;left:0;top:136px;width:1200px;height:556px;background:linear-gradient(90deg,#dfe3e6 0%,#c9cdd0 40%,#9aa3ab 60%,#d7dadb 100%)}
.hero-card{position:absolute;left:110px;top:140px;width:317px;height:272px;background:var(--brand);color:var(--white);padding:18px 19px}
.hero-card .eyebrow{font-size:17px}
.hero-card h1{font-size:44px;line-height:46px;font-weight:700;margin-top:8px}
.hero-card p{font-size:14px;line-height:18px;margin-top:10px}
.btn{display:inline-flex;align-items:center;gap:14px;height:36px;padding:0 12px;border:2px solid currentColor;font-size:14px;color:inherit;text-decoration:none}
.hero-card .btn{margin-top:16px}

.service-tabs{position:absolute;left:115px;top:653px;display:flex;gap:10px;z-index:5}
.tab{position:relative;width:236px;height:64px;background:var(--tab);display:flex;align-items:center;gap:14px;padding-left:40px;font-size:15px;line-height:18px;color:#333}
.tab b{color:var(--brand)}
.tab.active{background:var(--brand);color:var(--white)}
.tab.active b{color:var(--white)}
.tab.active::before{content:"";position:absolute;left:102px;top:-12px;border:12px solid transparent;border-top:0;border-bottom-color:var(--brand)}

/* about */
.about{position:absolute;left:0;top:692px;width:1200px;height:322px;background:var(--soft);text-align:center}
.section-title{font-size:34px;font-weight:400;color:var(--ink)}
.section-title b{color:var(--brand)}
.about .section-title{margin-top:80px}
.about p{font-size:15px;line-height:21px;color:#333;width:860px;margin:16px auto 0}
.about .btn{margin-top:16px;color:var(--brand);font-size:14px}

/* kiosk feature */
.feature{position:absolute;left:0;top:1014px;width:1200px;height:406px;background:linear-gradient(90deg,#c5c9cc 0%,#e3e6e8 35%,#f4f5f6 60%,#eef0f1 100%)}
.feature-text{position:absolute;left:622px;top:80px;width:470px}
.feature-text p{font-size:15px;line-height:21px;color:#333;margin-top:14px}
.feature-text .btn{margin-top:20px;color:var(--brand)}

/* testimonials */
.testimonials{position:absolute;left:0;top:1420px;width:1200px;height:428px;background:var(--white)}
.testimonials .section-title{position:absolute;left:0;width:1200px;top:52px;text-align:center}
.carousel{position:absolute;left:192px;top:148px;width:811px;height:113px;border:1px solid #ddd;background:var(--white)}
.avatar{position:absolute;top:10px;width:80px;height:93px}
.avatar.featured{top:-22px;width:156px;height:152px;border:2px solid var(--brand)}
.arrow{position:absolute;top:193px}
.quote-name{position:absolute;left:192px;top:320px;font-size:21px;font-weight:700;color:var(--brand);white-space:nowrap}
.quote-role{position:absolute;left:192px;top:347px;font-size:15px}
.quote-rule{position:absolute;left:348px;top:312px;width:1px;height:60px;background:#ccc}
.quote-text{position:absolute;left:370px;top:310px;width:640px;font-size:15px;line-height:21px;font-style:italic;color:#777}

/* locator */
.locator{position:absolute;left:0;top:1848px;width:1200px;height:539px;background:linear-gradient(135deg,#ece7d8 0%,#e6e4d2 55%,#cfdfe8 80%,#a9c7ea 100%)}
.filter-panel{position:absolute;left:181px;top:14px;width:205px;height:192px;background:var(--white);box-shadow:0 1px 4px rgba(0,0,0,.3);font-size:12px}
.filter-panel .row{height:40px;border-bottom:1px solid #ddd;display:flex;align-items:center;justify-content:space-between;padding:0 12px}
.filter-panel .head{height:56px;font-size:10px;color:#555}
.filter-panel .head a{color:#1f78d1;text-decoration:none}
.select-btn{position:absolute;right:10px;bottom:14px;width:88px;height:34px;background:#1f8ae6;color:var(--white);font-size:13px;text-align:center;line-height:34px}
.search-bar{position:absolute;left:400px;top:28px;width:620px;height:40px;background:var(--white);box-shadow:0 1px 4px rgba(0,0,0,.3);display:flex;align-items:center;padding:0 12px;font-size:11px;color:#999}
.search-note{position:absolute;left:393px;top:77px;width:627px;height:34px;background:#2b2b2b;color:var(--white);font-size:10px;display:flex;align-items:center;padding-left:152px}
.stores-card{position:absolute;left:178px;top:479px;width:846px;height:60px;background:var(--white);font-size:24px;padding:20px 24px 0}

/* footer */
.site-footer{position:absolute;left:0;top:2387px;width:1200px;height:110px;background:var(--brand);color:var(--white)}
.footer-ask{position:absolute;left:110px;top:22px;font-size:24px;line-height:36px}
.footer-ask b{font-weight:700}
.footer-phone{position:absolute;left:810px;top:40px;display:flex;align-items:center;gap:18px;font-size:30px;font-weight:700}
.to-top{position:absolute;left:1126px;top:36px;width:40px;height:40px;background:var(--brand-dark);display:flex;align-items:center;justify-content:center}
.legal{position:absolute;left:0;top:2497px;width:1200px;height:45px;background:var(--footer-dark);color:var(--white);font-size:13px}
.legal .copy{position:absolute;left:110px;top:15px}
.legal .links{position:absolute;right:110px;top:15px}
</style>
</head>
<body>

<header class="site-header">
  <div class="brand"><span class="brand-mark"></span>TAVRO</div>
  <div class="header-phone">
    <svg width="20" height="20" viewBox="0 0 24 24"><path fill="#0b5e9c" d="M6.6 10.8a15 15 0 0 0 6.6 6.6l2.2-2.2c.3-.3.7-.4 1-.2 1.1.4 2.3.6 3.6.6.6 0 1 .4 1 1V20c0 .6-.4 1-1 1A17 17 0 0 1 3 4c0-.6.4-1 1-1h3.5c.6 0 1 .4 1 1 0 1.3.2 2.5.6 3.6.1.3 0 .7-.2 1z"/></svg>
    555-014-2280
  </div>
  <div class="social"><span></span><span></span><span></span><span></span></div>
  <nav class="main-nav">
    <a class="active" href="#">HOME</a>
    <a href="#">ABOUT US</a>
    <a href="#">SERVICES</a>
    <a href="#">KIOSK</a>
    <a href="#">CONTACT US</a>
  </nav>
</header>

<section class="hero" role="img" aria-label="Photo of two businesswomen using a touchscreen kiosk in a bright terminal">
  <div class="hero-card">
    <div class="eyebrow">Use Our Mobile Kiosk Technology</div>
    <h1>Mobile Kiosk Technology</h1>
    <p>Lorem ipsum dolor sit amet, consectet ur adipiscing elit, sed do eiusmod tem incididunt ut labore.</p>
    <a class="btn" href="#">Read More <svg width="8" height="12" viewBox="0 0 8 12"><path d="M1 1l5 5-5 5" fill="none" stroke="currentColor" stroke-width="2"/></svg></a>
  </div>
</section>

<section class="about">
  <h2 class="section-title">About <b>TAVRO</b></h2>
  <p>Where you need it. When you need it. TAVRO kiosks provide easy access for you to run your mobile office. Whether you nees to access the internet to research&nbsp; information, access email, download document or pay bills, were here to help, TAVRO kiosks also provide you with the ability to print, scan, copy and fax document you need quickly,<br>All at the touch of a button.</p>
  <a class="btn" href="#">Read More <svg width="8" height="12" viewBox="0 0 8 12"><path d="M1 1l5 5-5 5" fill="none" stroke="currentColor" stroke-width="2"/></svg></a>
</section>

<div class="service-tabs">
  <div class="tab active">
    <svg width="22" height="30" viewBox="0 0 22 30"><rect x="3" y="1" width="16" height="28" fill="#fff"/><rect x="6" y="5" width="10" height="7" fill="#0b5e9c"/></svg>
    <div>KIOSK<br>TECHNOLOGY</div>
  </div>
  <div class="tab">
    <svg width="32" height="28" viewBox="0 0 32 28"><rect x="8" y="1" width="16" height="8" fill="#0b5e9c"/><rect x="1" y="9" width="30" height="12" rx="2" fill="#0b5e9c"/><rect x="8" y="17" width="16" height="10" fill="#fff" stroke="#0b5e9c" stroke-width="2"/></svg>
    <div>DOCUMENTS<br><b>PRINTING</b></div>
  </div>
  <div class="tab">
    <svg width="28" height="30" viewBox="0 0 28 30"><path d="M4 1h14l6 6v14H4z" fill="#0b5e9c"/><rect x="1" y="21" width="26" height="8" fill="#0b5e9c"/></svg>
    <div>PAPERS<br><b>SCANNING</b></div>
  </div>
  <div class="tab">
    <svg width="30" height="30" viewBox="0 0 30 30"><rect x="1" y="6" width="7" height="23" fill="#0b5e9c"/><rect x="10" y="1" width="19" height="28" fill="#0b5e9c"/><rect x="13" y="5" width="13" height="6" fill="#fff"/><rect x="13" y="15" width="13" height="10" fill="#fff"/></svg>
    <div>DOCUMENTS<br><b>FAXING</b></div>
  </div>
</div>

<section class="feature" role="img" aria-label="Photo of a businesswoman using a touchscreen kiosk">
  <div class="feature-text">
    <h2 class="section-title">Our <b>Mobile Kiosk</b></h2>
    <p>Lorem ipsum dolor sit amet, consectetur adipiscing elit, sed do eius mod tempor incididunt ut labore et dolore magna aliqua. Ut enim ad minim veniam, quis nostrud exercitation ullamco laboris nisi ut aliquip ex ea commodo consequatquis nostrud exercitation ullamco.</p>
    <a class="btn" href="#">Read More <svg width="8" height="12" viewBox="0 0 8 12"><path d="M1 1l5 5-5 5" fill="none" stroke="currentColor" stroke-width="2"/></svg></a>
  </div>
</section>

<section class="testimonials">
  <h2 class="section-title">See What Our <b>Client Says</b></h2>
  <svg class="arrow" style="left:135px" width="16" height="24" viewBox="0 0 16 24"><path d="M13 2L4 12l9 10" fill="none" stroke="#aaa" stroke-width="3"/></svg>
  <svg class="arrow" style="left:1045px" width="16" height="24" viewBox="0 0 16 24"><path d="M3 2l9 10-9 10" fill="none" stroke="#aaa" stroke-width="3"/></svg>
  <div class="carousel">
    <div class="avatar" role="img" aria-label="Client portrait" style="left:10px;background:#c8c2bb"></div>
    <div class="avatar" role="img" aria-label="Client portrait" style="left:98px;background:#bdb6ae"></div>
    <div class="avatar featured" role="img" aria-label="Featured client portrait" style="left:190px;background:#a9a9ab"></div>
    <div class="avatar" role="img" aria-label="Client portrait" style="left:352px;background:#cfc8c0"></div>
    <div class="avatar" role="img" aria-label="Client portrait" style="left:440px;background:#d6d0c9"></div>
    <div class="avatar" role="img" aria-label="Client portrait" style="left:528px;background:#c3bcb4"></div>
    <div class="avatar" role="img" aria-label="Client portrait" style="left:616px;background:#d0cbc6"></div>
    <div class="avatar" role="img" aria-label="Client portrait" style="left:704px;background:#c9c4be;width:95px"></div>
  </div>
  <div class="quote-name">Clara Denton</div>
  <div class="quote-role">Lorem Ipsum</div>
  <div class="quote-rule"></div>
  <p class="quote-text">Lorem Ipsum is simply dummy text of the printing and typesetting industry. Lorem Ipsum has been the industry's standard dummy text ever since the book. Lorem Ipsum is simply dummy text of the printing and typesetting industry.</p>
</section>

<section class="locator" role="img" aria-label="Road map of the south-eastern United States showing store locations">
  <div class="filter-panel">
    <div class="row head"><div>0 of 0 outlets<br><a href="#">Show All</a></div><a href="#">Clear All</a></div>
    <div class="row">By Region <svg width="14" height="8" viewBox="0 0 14 8"><path d="M1 1l6 6 6-6" fill="none" stroke="#999" stroke-width="2"/></svg></div>
    <div class="row">Category <svg width="14" height="8" viewBox="0 0 14 8"><path d="M1 1l6 6 6-6" fill="none" stroke="#999" stroke-width="2"/></svg></div>
    <div class="select-btn">SELECT</div>
  </div>
  <div class="search-bar">Search for nearby stores</div>
  <div class="search-note">No nearby were found. Why not try using our search function above?</div>
  <div class="stores-card">Stores near you</div>
</section>

<footer class="site-footer">
  <div class="footer-ask">Questions?<br>Feel Free To Contact Us At <b>hello@tavro-kiosk.com</b></div>
  <div class="footer-phone">
    <svg width="36" height="36" viewBox="0 0 24 24"><path fill="none" stroke="#fff" stroke-width="1.6" d="M6.6 10.8a15 15 0 0 0 6.6 6.6l2.2-2.2c.3-.3.7-.4 1-.2 1.1.4 2.3.6 3.6.6.6 0 1 .4 1 1V20c0 .6-.4 1-1 1A17 17 0 0 1 3 4c0-.6.4-1 1-1h3.5c.6 0 1 .4 1 1 0 1.3.2 2.5.6 3.6.1.3 0 .7-.2 1z"/></svg>
    555-014-2280
  </div>
  <div class="to-top"><svg width="14" height="9" viewBox="0 0 14 9"><path d="M1 8l6-6 6 6" fill="none" stroke="#fff" stroke-width="2"/></svg></div>
</footer>
<div class="legal">
  <span class="copy">Copyright 2015 TAVRO. All Rights reserved</span>
  <span class="links">Privacy &amp; Terms</span>
</div>

</body>
</html>
```